TALLVEX MOTOR OIL LABEL

I am launching a new motor oil product called TallVex and I would like your help in designing the packaging. The product is aimed at delivering high-performance results for vehicles, and I want the packaging to reflect the premium quality and reliability of TallVex. The design should be modern, dynamic, and appeal to car enthusiasts, while also communicating trust and innovation. I’m looking for a sleek and professional look that stands out on the shelf. Please incorporate elements that highlight its efficiency and performance, with bold typography and striking colors to grab attention.
I also need a logo for the name TallVex, and I would like your help in choosing the right colors for the packaging. The logo should be bold, memorable, and represent the strength and high performance of the product. When it comes to the packaging colors, I want something that is both eye-catching and conveys a sense of power and reliability, while also appealing to car enthusiasts. Your guidance in selecting the perfect color scheme to match the brand identity will be greatly appreciated.
The types of oils I plan to offer are available in the following sizes: 1 liter, 4 liters, and 5 liters.

• 10W40 Synthetic Blend High Mileage
• 20W50 Synthetic Blend High Mileage
• 10W30 Synthetic Blend High Mileage
• 5W30 Synthetic Blend High Mileage
• 5W20 Synthetic Blend High Mileage

Additionally, I will offer

Additionally, I will offer a
0W16 FULL SYNTHETIC
OW20 FULL SYNTHETIC
5W20 FULL SYNTHETIC
5W30 FULL SYNTHETIC
5W40 FULL SYNTHETIC
0W40 FULL SYNTHETIC
AND HD MOTOR OIL
15W40 HAVEY DUTY DIESEL ENGINE OIL SYNTHETIC BLEND
5W40 HAVEY DUTY DIESEL ENGINE OIL FULL SYNTHETIC

Font styles to use
Serif

Colors
0054AA
0677BA
7BADD7
CADEEF
E8F1F8
59FF00
82FF00
B8FF75
E3FFCB
F4FFEA
FFF300
FFF600
FEFA6F
FFFEC7
FFFEE8
FFC000
F8CF3A
FAE287
FDF2CF
FEFAEE
F0912C
F2A743
F7CA91
FBE8D2
FDF5EE
EB3D1F
EC4F4E
F09395
F8D3D4
FCEDEE

```html
<!DOCTYPE html>
<html lang="en">
<head>
<meta charset="utf-8">
<title>TallVex Synthetic Oil – Label Range</title>
<link rel="stylesheet" href="https://fonts.googleapis.com/css2?family=Oswald:wght@500;600;700&family=Roboto+Condensed:wght@700&display=swap">
<style>
  :root {
    --canvas: #ffffff;
    --label-black: #141414;
    --stripe-white: #ffffff;
    --stripe-red: #eb3d1f;
    --accent-orange: #f2a743;
    --splash-orange: #f0912c;
    --splash-deep: #3a2a14;
    --pill-text: #eb3d1f;
    --badge-text: #141414;
  }
  html, body {
    margin: 0;
    width: 1200px;
    height: 927px;
    overflow: hidden;
    background: var(--canvas);
  }
  .label-range {
    position: relative;
    width: 1200px;
    height: 927px;
    display: flex;
    align-items: flex-end;
    justify-content: center;
    gap: 70px;
    box-sizing: border-box;
    padding-bottom: 150px;
  }
  .label { display: block; }
  .label--5l { width: 360px; }
  .label--4l { width: 340px; }
  .label--1l { width: 240px; }
  .brand-name {
    font-family: "Oswald", sans-serif;
    font-weight: 600;
    fill: var(--stripe-white);
  }
  .product-type {
    font-family: "Oswald", sans-serif;
    font-weight: 600;
    fill: var(--accent-orange);
  }
  .grade {
    font-family: "Oswald", sans-serif;
    font-weight: 700;
    fill: var(--accent-orange);
  }
  .grade-desc {
    font-family: "Roboto Condensed", sans-serif;
    font-weight: 700;
    fill: var(--stripe-white);
  }
  .volume-badge text {
    font-family: "Oswald", sans-serif;
    font-weight: 700;
    fill: var(--badge-text);
  }
  .performance-pill text {
    font-family: "Oswald", sans-serif;
    font-weight: 600;
    fill: var(--pill-text);
  }
</style>
</head>
<body>
<main class="label-range">

  <!-- 5 litre label -->
  <svg class="label label--5l" viewBox="0 0 410 590" aria-label="TallVex 5 litre label">
    <defs>
      <linearGradient id="splash-5" x1="0" y1="0" x2="1" y2="0">
        <stop offset="0" stop-color="var(--splash-orange)"/>
        <stop offset="0.6" stop-color="var(--accent-orange)"/>
        <stop offset="1" stop-color="var(--splash-deep)"/>
      </linearGradient>
    </defs>
    <polygon points="0,95 410,0 410,590 0,590" fill="var(--label-black)"/>
    <g class="stripes-top">
      <polygon points="0,120 410,17.5 410,25.5 0,128" fill="var(--stripe-white)"/>
      <polygon points="0,136 410,33.5 410,39.5 0,142" fill="var(--stripe-red)"/>
      <polygon points="0,148 410,45.5 410,50.5 0,153" fill="var(--stripe-red)"/>
    </g>
    <polygon class="stripe-mid" points="0,300 410,197.5 410,203.5 0,306" fill="var(--stripe-red)"/>
    <g class="stripes-bottom">
      <polygon points="0,385 410,282.5 410,294.5 0,397" fill="var(--stripe-white)"/>
      <polygon points="0,404 410,301.5 410,307.5 0,410" fill="var(--stripe-red)"/>
      <polygon points="0,416 410,313.5 410,318.5 0,421" fill="var(--stripe-red)"/>
    </g>
    <text class="brand-name" x="30" y="272" font-size="104" textLength="330" lengthAdjust="spacingAndGlyphs" transform="rotate(-14.04 30 272)">TALLVEX</text>
    <text class="product-type" x="70" y="355" font-size="50" textLength="290" lengthAdjust="spacingAndGlyphs" transform="rotate(-14.04 70 355)">SYNTHETIC OIL</text>
    <text class="grade" x="352" y="385" font-size="26" text-anchor="end">5w20</text>
    <text class="grade-desc" x="385" y="410" font-size="10.5" text-anchor="end">Synthetic Blend High Mileage</text>
    <rect x="0" y="440" width="410" height="150" fill="url(#splash-5)" role="img" aria-label="Orange oil splash around an engine piston"/>
    <g class="volume-badge">
      <circle cx="62" cy="512" r="27" fill="var(--stripe-white)"/>
      <text x="62" y="522" font-size="26" text-anchor="middle">5 L</text>
    </g>
    <g class="performance-pill">
      <rect x="0" y="548" width="150" height="22" rx="11" fill="var(--stripe-white)"/>
      <text x="16" y="563" font-size="11">HIGHT PERFORMANCE</text>
    </g>
  </svg>

  <!-- 4 litre label -->
  <svg class="label label--4l" viewBox="0 0 410 530" aria-label="TallVex 4 litre label">
    <defs>
      <linearGradient id="splash-4" x1="0" y1="0" x2="1" y2="0">
        <stop offset="0" stop-color="var(--splash-orange)"/>
        <stop offset="0.6" stop-color="var(--accent-orange)"/>
        <stop offset="1" stop-color="var(--splash-deep)"/>
      </linearGradient>
    </defs>
    <polygon points="0,92 410,0 410,530 0,530" fill="var(--label-black)"/>
    <g class="stripes-top">
      <polygon points="0,110 410,7.5 410,15.5 0,118" fill="var(--stripe-white)"/>
      <polygon points="0,126 410,23.5 410,29.5 0,132" fill="var(--stripe-red)"/>
      <polygon points="0,138 410,35.5 410,40.5 0,143" fill="var(--stripe-red)"/>
    </g>
    <polygon class="stripe-mid" points="0,272 410,169.5 410,175.5 0,278" fill="var(--stripe-red)"/>
    <g class="stripes-bottom">
      <polygon points="0,350 410,247.5 410,259.5 0,362" fill="var(--stripe-white)"/>
      <polygon points="0,369 410,266.5 410,272.5 0,375" fill="var(--stripe-red)"/>
      <polygon points="0,381 410,278.5 410,283.5 0,386" fill="var(--stripe-red)"/>
    </g>
    <text class="brand-name" x="30" y="246" font-size="98" textLength="320" lengthAdjust="spacingAndGlyphs" transform="rotate(-14.04 30 246)">TALLVEX</text>
    <text class="product-type" x="70" y="320" font-size="46" textLength="270" lengthAdjust="spacingAndGlyphs" transform="rotate(-14.04 70 320)">SYNTHETIC OIL</text>
    <text class="grade" x="350" y="345" font-size="26" text-anchor="end">5w20</text>
    <text class="grade-desc" x="385" y="368" font-size="10.5" text-anchor="end">Synthetic Blend High Mileage</text>
    <rect x="0" y="392" width="410" height="138" fill="url(#splash-4)" role="img" aria-label="Orange oil splash around an engine piston"/>
    <g class="volume-badge">
      <circle cx="62" cy="458" r="27" fill="var(--stripe-white)"/>
      <text x="62" y="468" font-size="26" text-anchor="middle">4 L</text>
    </g>
    <g class="performance-pill">
      <rect x="0" y="494" width="150" height="22" rx="11" fill="var(--stripe-white)"/>
      <text x="16" y="509" font-size="11">HIGHT PERFORMANCE</text>
    </g>
  </svg>

  <!-- 1 litre label -->
  <svg class="label label--1l" viewBox="0 0 280 380" aria-label="TallVex 1 litre label">
    <defs>
      <linearGradient id="splash-1" x1="0" y1="0" x2="1" y2="0">
        <stop offset="0" stop-color="var(--splash-orange)"/>
        <stop offset="0.6" stop-color="var(--accent-orange)"/>
        <stop offset="1" stop-color="var(--splash-deep)"/>
      </linearGradient>
    </defs>
    <polygon points="0,62 280,0 280,380 0,380" fill="var(--label-black)"/>
    <g class="stripes-top">
      <polygon points="0,76 280,6 280,12 0,82" fill="var(--stripe-white)"/>
      <polygon points="0,87 280,17 280,21 0,91" fill="var(--stripe-red)"/>
      <polygon points="0,95 280,25 280,28 0,98" fill="var(--stripe-red)"/>
    </g>
    <polygon class="stripe-mid" points="0,196 280,126 280,130 0,200" fill="var(--stripe-red)"/>
    <g class="stripes-bottom">
      <polygon points="0,250 280,180 280,188 0,258" fill="var(--stripe-white)"/>
      <polygon points="0,263 280,193 280,197 0,267" fill="var(--stripe-red)"/>
      <polygon points="0,271 280,201 280,204 0,274" fill="var(--stripe-red)"/>
    </g>
    <text class="brand-name" x="20" y="178" font-size="66" textLength="220" lengthAdjust="spacingAndGlyphs" transform="rotate(-14.04 20 178)">TALLVEX</text>
    <text class="product-type" x="48" y="229" font-size="31" textLength="180" lengthAdjust="spacingAndGlyphs" transform="rotate(-14.04 48 229)">SYNTHETIC OIL</text>
    <text class="grade" x="240" y="250" font-size="17" text-anchor="end">5w20</text>
    <text class="grade-desc" x="265" y="266" font-size="7" text-anchor="end">Synthetic Blend High Mileage</text>
    <rect x="0" y="284" width="280" height="96" fill="url(#splash-1)" role="img" aria-label="Orange oil splash around an engine piston"/>
    <g class="volume-badge">
      <circle cx="44" cy="330" r="18" fill="var(--stripe-white)"/>
      <text x="44" y="337" font-size="17" text-anchor="middle">1 L</text>
    </g>
    <g class="performance-pill">
      <rect x="0" y="356" width="104" height="15" rx="7.5" fill="var(--stripe-white)"/>
      <text x="11" y="366.5" font-size="7.5">HIGHT PERFORMANCE</text>
    </g>
  </svg>

</main>
</body>
</html>
```